Zielgruppe
Tobias Fink Personal Training.
Personaltraining für Bürotätige / leitende Positionen.
Rücken- und Haltungstraining.
Zielgruppe: Herren mittleren Alters, gehobene Klasse.
Aufgabenstellung
Schlicht, elegant, hochwertig
Gerne Logo eingearbeitet.
Schwarz / Gold / Weiß

```html
<!DOCTYPE html>
<html lang="de">
<head>
<meta charset="utf-8">
<title>Tobias Fink Personal Training – Visitenkarte</title>
<link href="https://fonts.googleapis.com/css2?family=Open+Sans:wght@400;600&display=swap" rel="stylesheet">
<style>
  :root {
    --backdrop: #c9c8c8;
    --paper: #ffffff;
    --charcoal: #333333;
    --gold: #c9a227;
    --ink: #3d3d3d;
    --ink-light: #777777;
    --web-text: #dddddd;
  }
  * { margin: 0; padding: 0; box-sizing: border-box; }
  html, body { width: 1200px; height: 900px; overflow: hidden; }
  body {
    background: var(--backdrop);
    font-family: "Open Sans", Arial, sans-serif;
    position: relative;
  }
  .card {
    position: absolute;
    top: 282px;
    width: 540px;
    height: 336px;
    overflow: hidden;
    box-shadow: 0 10px 24px rgba(0,0,0,.22);
  }
  .card--front { left: 40px; background: var(--paper); }
  .card--back { left: 620px; background: var(--charcoal); }

  /* front */
  .band { position: absolute; background: var(--charcoal); }
  .band--top { left: 0; top: 0; width: 318px; height: 34px; }
  .band--side { right: 0; top: 178px; width: 70px; height: 22px; }
  .gold-rule { position: absolute; height: 2px; background: var(--gold); }
  .gold-rule--top { left: 0; top: 40px; width: 318px; }
  .gold-rule--side { right: 0; top: 204px; width: 70px; }
  .web {
    position: absolute; left: 18px; top: 9px;
    color: var(--web-text); font-size: 11px; font-weight: 600; letter-spacing: .3px;
  }
  .brand-name {
    position: absolute; white-space: nowrap;
    color: var(--gold); font-size: 16px; font-weight: 600; line-height: 20px;
  }
  .card--front .brand-name { left: 222px; top: 179px; }
  .person { position: absolute; left: 30px; top: 66px; color: var(--ink); }
  .person__name { font-size: 20px; font-weight: 400; }
  .person__role { font-size: 10px; color: var(--ink-light); margin-top: 1px; }
  .address {
    position: absolute; left: 30px; top: 140px;
    color: var(--ink); font-size: 15px; line-height: 1.4; font-style: normal;
  }
  .contact {
    position: absolute; left: 300px; top: 240px; list-style: none;
    color: var(--ink); font-size: 17px; line-height: 1.45;
  }
  .contact li { display: flex; align-items: center; gap: 10px; }
  .contact svg { width: 16px; height: 16px; fill: var(--gold); flex: none; }

  /* back */
  .back-rule { position: absolute; height: 2px; background: var(--gold); }
  .back-rule--left { left: 0; top: 168px; width: 140px; }
  .back-rule--right { right: 0; top: 168px; width: 140px; }
  .card--back .brand-name { left: 154px; top: 159px; }
</style>
</head>
<body>

<section class="card card--front" aria-label="Vorderseite">
  <div class="band band--top"><span class="web">www.tfpt-training.de</span></div>
  <div class="gold-rule gold-rule--top"></div>
  <div class="band band--side"></div>
  <div class="gold-rule gold-rule--side"></div>

  <p class="brand-name">Tobias Fink Personal Training</p>

  <div class="person">
    <p class="person__name">Jonas Weber</p>
    <p class="person__role">Geschäftsführer</p>
  </div>

  <address class="address">
    TFPT Ltd<br>Birkenweg 27<br>A-4711 Lindenhain
  </address>

  <ul class="contact">
    <li><svg viewBox="0 0 24 24"><path d="M6.6 10.8a15 15 0 0 0 6.6 6.6l2.2-2.2c.3-.3.7-.4 1-.2 1.1.4 2.3.6 3.6.6.6 0 1 .4 1 1V20c0 .6-.4 1-1 1A17 17 0 0 1 3 4c0-.6.4-1 1-1h3.5c.6 0 1 .4 1 1 0 1.3.2 2.5.6 3.6.1.3 0 .7-.2 1z"/></svg>04913/278 40-11</li>
    <li><svg viewBox="0 0 24 24"><path d="M6 2h12v6H6zM3 9h18v9h-3v4H6v-4H3zm5 6v5h8v-5z"/></svg>04913/278 40-19</li>
    <li><svg viewBox="0 0 24 24"><path d="M2 5h20v14H2zm2 2v.5l8 5 8-5V7zm0 2.8V17h16V9.8l-8 5z"/></svg>info@tfpt-training.de</li>
  </ul>
</section>

<section class="card card--back" aria-label="Rückseite">
  <div class="back-rule back-rule--left"></div>
  <p class="brand-name">Tobias Fink Personal Training</p>
  <div class="back-rule back-rule--right"></div>
</section>

</body>
</html>
```